your logo, sewn on, your garments ,today , shop

signage

media road side hoarding signs

simple easy to read when driving

be able to read from 100 mtres/yards

see clip hive

amber sail

explains a little what we do here

Target Market(s)

we embroider accross a wide range
from
all types
small business
sports clubs
scouts ,guides
groups
range is very wide

Industry/Entity Type

Shop

Requirements
Must have
• clear information
• be able to understand what we do clearly
• its new to most people so they are confused
• at to whats on offer to sew there logo on there own clothes
• customers are either
• new or existing on our computors
• existing get done faster
• we have a while you wait service
• but the time will take
• depends on amount of work at the time
• and how many logos
• they average 45 minutes each so three logo same garment will be over 2 hours
• so please added on somewhere
• Either
• T & C Apply
• or
• Terms and Conditions Apply
• we have 75,000 customer original logos here that we sew already for customers
• we use road signs 52 weeks of the year to remind people
• a . we are still here
• b .we still have there logos
• c .own garments its new to most of them ?we now can sew on to any of the bargains they can find in sales etc or in the larger supermarkets
Nice to have
• simple logo of a needle thread
Should not have
• should be complicated
• everyone is a individual
• we like them to make there own judgement on there own logos

```html
<!DOCTYPE html>
<html lang="en">
<head>
<meta charset="utf-8">
<title>Your Logo Sewn On Your Clothes – Roadside Hoarding</title>
<link rel="stylesheet" href="https://fonts.googleapis.com/css2?family=Open+Sans:wght@700&family=Kaushan+Script&display=swap">
<style>
  :root {
    --stage: #59595b;
    --sky-deep: #2a64a8;
    --sky-light: #4f94d2;
    --aqua: #1fa3de;
    --lime: #b5d334;
    --white: #ffffff;
    --thread-red: #d9161d;
    --brand-navy: #2e3192;
    --machine-light: #e9e8e3;
    --fabric-navy: #27324a;
  }
  * { margin: 0; padding: 0; box-sizing: border-box; }
  html, body { width: 1200px; height: 999px; overflow: hidden; background: var(--stage); }
  .canvas { position: relative; width: 1200px; height: 999px; }
  .hoarding-art { position: absolute; inset: 0; }
  .headline {
    position: absolute;
    font-family: "Open Sans", Arial, sans-serif;
    font-weight: 700;
    color: var(--white);
    font-size: 55px;
    line-height: 75px;
    letter-spacing: 1px;
  }
  .headline--logo { left: 625px; top: 236px; }
  .headline--clothes { left: 860px; top: 486px; text-align: center; }
  .script-sewn-on {
    position: absolute;
    left: 470px; top: 380px;
    width: 660px;
    text-align: center;
    font-family: "Kaushan Script", cursive;
    font-size: 158px;
    line-height: 1;
    color: var(--thread-red);
    transform: rotate(-29deg);
    transform-origin: center;
  }
  .brand-name {
    position: absolute;
    left: 700px; top: 686px;
    width: 180px;
    text-align: center;
    font-family: "Open Sans", Arial, sans-serif;
    font-weight: 700;
    font-size: 32px;
    line-height: 38px;
    color: var(--brand-navy);
  }
</style>
</head>
<body>
<main class="canvas">
  <svg class="hoarding-art" width="1200" height="999" viewBox="0 0 1200 999">
    <defs>
      <linearGradient id="sky" x1="0" y1="1" x2="1" y2="0">
        <stop offset="0" stop-color="var(--sky-light)"/>
        <stop offset="1" stop-color="var(--sky-deep)"/>
      </linearGradient>
      <linearGradient id="workshop" x1="0" y1="0" x2="0.6" y2="1">
        <stop offset="0" stop-color="var(--machine-light)"/>
        <stop offset="0.55" stop-color="#c9ccd0"/>
        <stop offset="1" stop-color="var(--fabric-navy)"/>
      </linearGradient>
      <clipPath id="board"><rect x="22" y="210" width="1156" height="579"/></clipPath>
    </defs>
    <g clip-path="url(#board)">
      <rect class="board-sky" x="22" y="210" width="1156" height="579" fill="url(#sky)"/>
      <path class="swoosh-aqua" d="M22,760 C180,720 300,690 420,670 L220,789 L22,789 Z" fill="var(--aqua)"/>
      <path class="swoosh-lime" d="M600,200 C570,430 420,660 22,752" fill="none" stroke="var(--lime)" stroke-width="22"/>
      <path class="swoosh-white" d="M585,200 C555,420 410,640 22,736" fill="none" stroke="var(--white)" stroke-width="16"/>
      <path class="workshop-photo" role="img" aria-label="Photo of a row of multi-head embroidery machines stitching dark garments in blue hoops"
            d="M22,200 H578 C548,415 405,630 22,728 Z" fill="url(#workshop)"/>
      <path class="footer-white" d="M215,789 C420,690 780,648 1178,670 V789 Z" fill="var(--white)"/>
      <path class="footer-lime" d="M225,792 C430,690 790,650 1180,676" fill="none" stroke="var(--lime)" stroke-width="9"/>
    </g>
    <rect x="22" y="210" width="1156" height="579" fill="none" stroke="#222" stroke-width="1"/>
  </svg>

  <h1 class="headline headline--logo">YOUR<br>LOGO</h1>
  <p class="script-sewn-on">Sewn On</p>
  <p class="headline headline--clothes">YOUR<br>CLOTHES</p>
  <p class="brand-name">AMBER<br>SAIL</p>
</main>
</body>
</html>
```